Business Card Design

We are a manufacturing company that has been in business for over 30 years, established in 1981. We are looking to increase our business with defence force, government, and the major telecoms so the card needs to present the company as being cutting edge, secure, and professional.
Industry/Entity Type
Defence
Contact Information for Business Card
Name Gareth Olsund
Phone 02 9374 6815
Fax 02 9457 3162
mobile 0438260517
Email Gary@Korvex.com.au
Webiste www.korvex.com.au
ABN 58 006 391 842
address: 17 Belcor Street Marlow Vale NSW 2581
"Manufacturer of Antennas, GPS, Microwave, Cable Assemblies, RF, Military, & Telecommunications"
Look and feel

```html
<!DOCTYPE html>
<html lang="en">
<head>
<meta charset="utf-8">
<title>Korvex Business Card</title>
<link rel="stylesheet" href="https://fonts.googleapis.com/css2?family=Open+Sans:wght@400;600&display=swap">
<style>
  :root {
    --navy: #16214f;
    --rust: #b5402a;
    --white: #ffffff;
    --grey-band: #d9d9d9;
    --ink: #2a2a2a;
    --backdrop: #e9e7e4;
  }
  * { box-sizing: border-box; margin: 0; padding: 0; }
  html, body { width: 1200px; height: 900px; overflow: hidden; }
  body {
    background: var(--backdrop);
    font-family: "Open Sans", Arial, sans-serif;
    color: var(--white);
    position: relative;
  }
  .card {
    position: absolute;
    left: 300px;
    width: 600px;
    height: 343px;
    background: var(--navy);
    overflow: hidden;
    box-shadow: 0 4px 14px rgba(0,0,0,0.18);
  }
  .card--front { top: 80px; }
  .card--back { top: 477px; }

  /* Front */
  .front-mark {
    position: absolute;
    left: 287px; top: 112px;
    width: 26px; height: 26px;
    background: var(--white);
  }
  .front-name {
    position: absolute;
    top: 168px; width: 100%;
    text-align: center;
    font-size: 27px;
    font-weight: 400;
    letter-spacing: 5px;
  }
  .web-band {
    position: absolute;
    left: 0; top: 280px;
    width: 100%; height: 36px;
    background: var(--rust);
    text-align: center;
    line-height: 36px;
    font-size: 19px;
    letter-spacing: 5px;
  }

  /* Back */
  .name-band {
    position: absolute;
    left: 28px; top: 60px;
    width: 572px; height: 38px;
    background: var(--rust);
    text-align: center;
    line-height: 38px;
    font-size: 23px;
    font-weight: 400;
  }
  .brand-block {
    position: absolute;
    left: 55px; top: 130px;
    width: 105px;
    text-align: center;
  }
  .brand-block__mark {
    width: 22px; height: 22px;
    background: var(--white);
    margin: 10px auto 22px;
  }
  .brand-block__tag {
    background: var(--rust);
    font-size: 13px;
    letter-spacing: 2.5px;
    padding: 3px 0;
  }
  .contact-list {
    position: absolute;
    left: 220px; top: 124px;
    list-style: none;
    border-left: 1.5px solid var(--white);
    padding-left: 14px;
  }
  .contact-list li {
    position: relative;
    font-size: 13.5px;
    line-height: 19px;
    white-space: nowrap;
  }
  .contact-list li.abn { font-size: 11.5px; }
  .contact-list .icon {
    position: absolute;
    left: -36px; top: 3px;
    width: 14px; height: 13px;
  }
  .contact-list .icon-text {
    position: absolute;
    left: -38px; top: 0;
    font-size: 8.5px;
  }
  .tagline-band {
    position: absolute;
    left: 0; top: 288px;
    width: 100%; height: 44px;
    background: var(--grey-band);
    color: var(--ink);
    text-align: center;
    font-size: 15px;
    line-height: 20px;
    padding-top: 2px;
  }
</style>
</head>
<body>

<section class="card card--front" aria-label="Card front">
  <div class="front-mark"></div>
  <div class="front-name">KORVEX</div>
  <div class="web-band">www.korvex.com.au</div>
</section>

<section class="card card--back" aria-label="Card back">
  <div class="name-band">GARETH OLSUND</div>

  <div class="brand-block">
    <div class="brand-block__mark"></div>
    <div class="brand-block__tag">KORVEX</div>
  </div>

  <ul class="contact-list">
    <li>
      <svg class="icon" viewBox="0 0 14 13" fill="#fff"><path d="M1 4 Q7 0 13 4 L11 6 L9 5 L9 3.5 Q7 3 5 3.5 L5 5 L3 6 Z"/><rect x="3" y="7" width="8" height="5" rx="1"/></svg>
      02 9374 6815
    </li>
    <li>
      <svg class="icon" viewBox="0 0 14 13" fill="#fff"><rect x="3.5" y="0" width="7" height="13" rx="1.2"/><rect x="5" y="1.5" width="4" height="6" fill="#16214f"/></svg>
      0438260517
    </li>
    <li>
      <svg class="icon" viewBox="0 0 14 13" fill="#fff"><rect x="3" y="0" width="8" height="4"/><rect x="0.5" y="4" width="13" height="6" rx="1"/><rect x="3" y="8" width="8" height="5" fill="#fff" stroke="#16214f" stroke-width="1"/></svg>
      02 9457 3162
    </li>
    <li>
      <svg class="icon" viewBox="0 0 14 13" fill="none" stroke="#fff" stroke-width="1.2"><circle cx="7" cy="6.5" r="5.8"/><rect x="3.8" y="4.3" width="6.4" height="4.4"/><path d="M3.8 4.3 L7 7 L10.2 4.3"/></svg>
      Gary@Korvex.com.au
    </li>
    <li>
      <svg class="icon" viewBox="0 0 14 13" fill="#fff"><path d="M7 0.5 L13.5 6.5 L11.5 6.5 L11.5 12.5 L8.5 12.5 L8.5 8.5 L5.5 8.5 L5.5 12.5 L2.5 12.5 L2.5 6.5 L0.5 6.5 Z"/></svg>
      17 Belcor Street, Marlow Vale, NSW 2581
    </li>
    <li class="abn">
      <span class="icon-text">ABN</span>
      58 006 391 842
    </li>
  </ul>

  <div class="tagline-band">
    Manufacturer of Antennas, GPS, Microwave, Cable Assemblies,<br>
    RF, Military, &amp; Telecommunications"
  </div>
</section>

</body>
</html>
```